Food Festival "Signature Cocktail" Booth Banner

Need a 3'x9'6" (36" tall x 114" wide) Outdoor Banner for a new "Signature Cocktail" booth at an outdoor food festival. Marlowe Onion Jubilee is a non profit festival and the World Record largest Garlic Festival with average of 100K attendees over 3 days. Actual drink served will vary from year to year, but banner for the booth with be reused each year so it will be non drink specific. Banner needs to catch attendee's attention both at a quick glance and from a distance outdoors to drive traffic and sales to the booth. It will be mounted above the sales window of a 10x10 Festival Booth on PVC frame (see attached pic for reference). "Signature Cocktail" is required text along with it being identified as a Marlowe Onion Jubilee booth either through use of attached logo (color can be modified) or "Marlowe Onion Jubilee" text since we also have for profit competing vendors. Banner will be full color print. Idea concepts: Neon Sign, Art Deco elegant, reclaimed wood...but open to any concepts. Festival website: https://marloweonionjubilee.example

Target Market(s)

Food Festival Attendees

Font styles to use
Decorative
Script
Other font styles liked:
• Neon, heavy weight fonts, open.

Colors

Designer to choose colors to be used in the design.

Requirements
Must have
• "Signature Cocktail" and "Marlowe Onion Jubilee" text or MOJ Logo provided, colors and layout that stands out and easily identifiable and readable from a long distance with strong text
Nice to have
• Vibrant engaging background,, ties to Garlic
Should not have
• Clip art, generic text

```html
<!DOCTYPE html>
<html lang="en">
<head>
<meta charset="utf-8">
<title>Signature Cocktail – Marlowe Onion Jubilee Booth Banner</title>
<link rel="stylesheet" href="https://fonts.googleapis.com/css2?family=Great+Vibes&family=Jost:wght@800&display=swap">
<style>
  :root {
    --wood-light: #9a8f82;
    --wood-mid: #7f7468;
    --wood-dark: #5e554c;
    --wood-warm: #8a7353;
    --ink: #3a302b;
    --glow: rgba(255, 246, 228, 0.55);
    --art-pink: #d3878b;
    --art-silver: #c9c6c2;
    --badge: #ffffff;
  }
  html, body {
    margin: 0;
    padding: 0;
    width: 1200px;
    height: 379px;
    overflow: hidden;
    background: #ffffff;
  }
  .banner {
    position: relative;
    width: 1200px;
    height: 379px;
    overflow: hidden;
  }
  .banner__wood {
    position: absolute;
    inset: 0;
    background:
      radial-gradient(ellipse 55% 60% at 52% 62%, rgba(160, 120, 70, 0.45), transparent 70%),
      linear-gradient(180deg, var(--wood-light) 0%, var(--wood-mid) 35%, var(--wood-warm) 60%, var(--wood-mid) 80%, var(--wood-dark) 100%);
  }
  .banner__cocktail-art {
    position: absolute;
    left: 12px;
    top: 10px;
    width: 190px;
    height: 350px;
    border-radius: 6px;
    background: linear-gradient(180deg,
      rgba(211, 135, 139, 0.85) 0%,
      rgba(211, 135, 139, 0.75) 35%,
      rgba(201, 198, 194, 0.55) 55%,
      rgba(201, 198, 194, 0.35) 100%);
  }
  .banner__type {
    position: absolute;
    inset: 0;
    width: 1200px;
    height: 379px;
  }
  .title-script {
    font-family: "Great Vibes", cursive;
    font-size: 200px;
    fill: var(--ink);
    paint-order: stroke;
    stroke: var(--glow);
    stroke-width: 3px;
  }
  .title-block {
    font-family: "Jost", sans-serif;
    font-weight: 800;
    font-size: 116px;
    fill: var(--ink);
    paint-order: stroke;
    stroke: var(--glow);
    stroke-width: 4px;
  }
  .festival-name {
    position: absolute;
    left: 1018px;
    top: 30px;
    width: 172px;
    margin: 0;
    font-family: "Jost", sans-serif;
    font-weight: 800;
    font-size: 33px;
    line-height: 1.08;
    text-align: center;
    text-transform: uppercase;
    color: var(--badge);
  }
</style>
</head>
<body>
  <main class="banner">
    <div class="banner__wood" role="img" aria-label="Weathered reclaimed wood plank background"></div>
    <div class="banner__cocktail-art" role="img" aria-label="Illustration of a pink martini cocktail garnished with two cherries"></div>

    <svg class="banner__type" viewBox="0 0 1200 379" aria-labelledby="banner-title">
      <title id="banner-title">Signature Cocktail</title>
      <text class="title-script" x="214" y="232" textLength="818" lengthAdjust="spacingAndGlyphs">Signature</text>
      <text class="title-block" x="164" y="349" textLength="988" lengthAdjust="spacing">COCKTAIL</text>
    </svg>

    <p class="festival-name">Marlowe Onion Jubilee</p>
  </main>
</body>
</html>
```